Candy Bar Desgin

We need a postcard desgin for my new company. I just started a Candy bar/buffet called Sweet Table By Mimi. My motto is Sweet Table by Mimi for the teeny treaty. I will be attending a bridal show where I can display my work so there will be brides there. So I want something to pop. Maybe can add vases filled with candy. Add 20% off an event you book for attending the bridal show. I want colors. Candy colors. My company also do chocolate fountain bars as well. My website to add is www.sweettablebymimi.example
Email sweettablebymimi@mailbox.example
Phone 555-014-2968

Target Market(s)

Brides

Industry/Entity Type

It Company

Requirements
Must have
• Must have my motto. And my contact information
Should not have
• No old style don't like times new roman. Use fun fonts

```html
<!DOCTYPE html>
<html lang="en">
<head>
<meta charset="utf-8">
<title>Sweet Table by Mimi — Bridal Show Postcard</title>
<link rel="stylesheet" href="https://fonts.googleapis.com/css2?family=Lobster&family=Didact+Gothic&family=Bungee&display=swap">
<style>
  :root {
    --lavender-bg: #dec5de;
    --stripe-blue: #b1b3dd;
    --stripe-pink: #ecd3e8;
    --top-rule: #d9363e;
    --ribbon-pink: #f4b9c9;
    --badge-blue: #a9a9d9;
    --ink: #2a2a2a;
    --contact-purple: #a65aae;
    --frame-pink: #f3b6c6;
    --white: #ffffff;
  }
  html, body { margin: 0; padding: 0; overflow: hidden; }
  body { width: 1200px; height: 931px; background: var(--lavender-bg); }
  .postcard {
    position: relative; width: 1200px; height: 931px; overflow: hidden;
    background: var(--lavender-bg);
  }
  .stripe-band {
    position: absolute; left: 0; top: 0; width: 1200px; height: 186px;
    background: repeating-linear-gradient(90deg, var(--stripe-pink) 0 27px, var(--stripe-blue) 27px 57px);
    border-top: 4px solid var(--top-rule);
    box-sizing: border-box;
  }
  .product-photo {
    position: absolute; left: 590px; top: 186px; width: 610px; height: 745px;
    background:
      radial-gradient(ellipse at 60% 45%, #e89ac0 0 18%, transparent 40%),
      radial-gradient(ellipse at 55% 85%, #e98cb6 0 25%, transparent 55%),
      linear-gradient(90deg, var(--lavender-bg) 0%, #cdb6cf 12%, #b9a7c9 60%, #d3cae6 100%);
  }
  .ribbon { position: absolute; left: 0; top: 0; width: 1200px; height: 931px; pointer-events: none; }
  .motto {
    position: absolute; left: 0; top: 40px; width: 1200px; margin: 0;
    text-align: center;
    font-family: "Lobster", cursive; font-weight: 400; font-size: 64px; line-height: 1;
    color: var(--white);
    text-shadow: 3px 3px 0 #111, -1px -1px 0 #111, 1px -1px 0 #111, -1px 1px 0 #111;
  }
  .offer-badge {
    position: absolute; left: 920px; top: 138px; width: 224px; height: 224px;
    border-radius: 50%; background: var(--badge-blue);
    display: flex; flex-direction: column; align-items: center; justify-content: center;
    font-family: "Bungee", sans-serif; color: var(--ink); text-align: center;
    text-shadow: 0 0 2px #fff;
  }
  .offer-badge .offer-amount { font-size: 40px; line-height: 1; margin-top: -10px; }
  .offer-badge .offer-terms { font-size: 19px; line-height: 1.35; margin-top: 6px; }
  .chocolate-photo {
    position: absolute; left: 17px; top: 172px; width: 316px; height: 316px;
    border-radius: 50%; border: 8px solid var(--frame-pink); box-sizing: border-box;
    background:
      radial-gradient(circle at 50% 32%, #7a4a2c 0 14%, transparent 22%),
      radial-gradient(circle at 50% 75%, #f2c889 0 20%, transparent 36%),
      linear-gradient(160deg, #c9a98a, #e9b6b0 60%, #f1d4c8);
  }
  .intro {
    position: absolute; left: 0; top: 212px; margin: 0;
    font-family: "Didact Gothic", sans-serif; font-size: 26px; line-height: 39px;
    color: var(--ink);
  }
  .intro span { display: block; white-space: nowrap; }
  .contact {
    position: absolute; left: 40px; top: 732px; width: 590px; margin: 0;
    font-family: "Didact Gothic", sans-serif; font-size: 32px; line-height: 43px;
    color: var(--contact-purple); text-align: center; font-style: normal;
  }
</style>
</head>
<body>
<main class="postcard">
  <div class="stripe-band"></div>
  <div class="product-photo" role="img" aria-label="Glass apothecary jars filled with pink and lavender candy on a pink polka-dot case"></div>

  <svg class="ribbon" viewBox="0 0 1200 931" aria-hidden="true">
    <polygon points="868,0 900,0 1060,280 1040,300" fill="var(--ribbon-pink)"/>
    <polygon points="1130,0 1165,0 1010,300 990,280" fill="var(--ribbon-pink)"/>
    <polygon points="1000,300 1030,300 960,480 935,460" fill="var(--ribbon-pink)"/>
    <polygon points="1020,300 1050,300 1110,460 1085,480" fill="var(--ribbon-pink)"/>
  </svg>

  <h1 class="motto">Sweet Table by Mimi for the teeny treaty</h1>

  <div class="offer-badge">
    <div class="offer-amount">20%off</div>
    <div class="offer-terms">any event you<br>book during the<br>bridal show.</div>
  </div>

  <div class="chocolate-photo" role="img" aria-label="Chocolate fountain surrounded by fruit and treats for dipping"></div>

  <p class="intro">
    <span style="margin-left:338px">Sweet Table by</span>
    <span style="margin-left:355px">Mimi will add fun</span>
    <span style="margin-left:362px">and color to your</span>
    <span style="margin-left:362px">reception and</span>
    <span style="margin-left:362px">bring you and</span>
    <span style="margin-left:353px">your guests back</span>
    <span style="margin-left:332px">to your childhood</span>
    <span style="margin-left:318px">roots. I promise it will</span>
    <span style="margin-left:66px">be visual feast filled with color, aroma</span>
    <span style="margin-left:66px">and the magic that only candy brings. I</span>
    <span style="margin-left:66px">provide my candy bars to&nbsp; your event at</span>
    <span style="margin-left:66px">any city.</span>
  </p>

  <address class="contact">
    Email sweettablebymimi@mailbox.example<br>
    Phone 555-014-2968<br>
    www.sweettablebymimi.example
  </address>
</main>
</body>
</html>
```